Bref créative
Stoneleaf Dwellings
Stationary, business cards, envelopes and t-shirts
Professional
Tim Valko
48217 Maplecrest Ln.
Ashbrook Falls, Oh 44287
valko@torvanmail.net
stoneleafdwellingsinc.com
Use the logo in the file

```html
<!DOCTYPE html>
<html lang="en">
<head>
<meta charset="utf-8">
<title>Stoneleaf Dwellings – Business Card</title>
<link rel="stylesheet" href="https://fonts.googleapis.com/css2?family=Arimo:ital,wght@0,400;0,700;1,700&family=Fredoka:wght@600&family=Tinos&display=swap">
<style>
  :root {
    --navy: #211d52;
    --gold: #c9a445;
    --olive-dark: #a9a12a;
    --olive-light: #dcd95a;
    --white: #ffffff;
    --ink: #1e1b3f;
    --text: #262626;
  }
  * { margin: 0; padding: 0; box-sizing: border-box; }
  html, body { width: 1200px; height: 686px; overflow: hidden; background: #ffffff; }
  .card {
    position: relative;
    width: 1200px;
    height: 686px;
    overflow: hidden;
    background: linear-gradient(100deg, var(--olive-dark) 0%, #bdb536 45%, var(--olive-light) 100%);
  }
  .card-shapes { position: absolute; inset: 0; }
  .brand-name {
    position: absolute;
    left: 66px;
    top: 172px;
    font-family: "Fredoka", sans-serif;
    font-weight: 600;
    font-size: 58px;
    color: var(--gold);
    white-space: nowrap;
  }
  .contact-person {
    position: absolute;
    left: 880px;
    top: 298px;
    color: var(--ink);
    font-family: "Arimo", sans-serif;
    white-space: nowrap;
  }
  .person-name { font-size: 44px; font-weight: 700; line-height: 1.1; letter-spacing: 1px; }
  .person-line { font-size: 23px; font-weight: 700; font-style: italic; line-height: 1.4; }
  .address {
    position: absolute;
    left: 400px;
    top: 490px;
    font-family: "Tinos", serif;
    font-size: 25px;
    line-height: 34px;
    color: var(--text);
    white-space: nowrap;
  }
  .web-contact {
    position: absolute;
    right: 18px;
    top: 598px;
    text-align: right;
    font-family: "Arimo", sans-serif;
    font-size: 23px;
    line-height: 30px;
    color: var(--text);
    white-space: nowrap;
  }
</style>
</head>
<body>
  <div class="card">
    <svg class="card-shapes" width="1200" height="686" viewBox="0 0 1200 686" aria-hidden="true">
      <path class="white-swoosh" fill="var(--white)" d="M0,476 C420,256 840,66 1200,8 V62 C860,122 470,312 0,540 Z"/>
      <path class="navy-field" fill="var(--navy)" d="M0,0 H1200 V12 C840,72 420,262 0,482 Z"/>
    </svg>

    <div class="brand-name">Stoneleaf Dwellings</div>

    <div class="contact-person">
      <div class="person-name">Tim Valko</div>
      <div class="person-line">Stoneleaf Dwelling</div>
      <div class="person-line">Built with Character</div>
    </div>

    <div class="address">
      48217 Maplecrest Ln.<br>
      Ashbrook Falls, Oh 44287<br>
      Phone: 440-555-0182<br>
      Cell: 440-555-0147<br>
      Fax: 440-555-0182
    </div>

    <div class="web-contact">
      www.stoneleafdwellingsinc.com<br>
      valko@torvanmail.net
    </div>
  </div>
</body>
</html>
```